Until now, Brisk Technology was exclusively geared towards marketing the self-warming toasty-toes insole. Corresponding designer material exists for this purpose, which is further used in this line of business. In the meantime, the business purpose has been expanded to include the following activities: "The company provides consulting services and takes on board mandates in the field of energy and information technology as well as personality-enhancing coaching." We now need a suitable stationery design (letterhead, business card) for this new business purpose. The design is intended to convey specialist knowledge and many years of experience

```html
<!DOCTYPE html>
<html lang="de">
<head>
<meta charset="utf-8">
<title>Brisk Technology GmbH – Stationery</title>
<link rel="stylesheet" href="https://fonts.googleapis.com/css2?family=Poppins:wght@400;500;600;700&display=swap">
<style>
  :root {
    --brand-blue: #2a93d5;
    --ink-dark: #2e2f31;
    --ink-body: #5a5c60;
    --paper: #ffffff;
    --stage-top: #ffffff;
    --stage-cards: #ecebe9;
    --stage-letter: #e6e7e9;
    --stage-env: #e9eaec;
    --edge: #dcdcdc;
    --faint-square: #ededee;
  }
  * { box-sizing: border-box; margin: 0; padding: 0; }
  html, body { width: 1200px; height: 3094px; overflow: hidden; }
  body { font-family: "Poppins", sans-serif; color: var(--ink-dark); position: relative; }

  .section { position: absolute; left: 0; width: 1200px; }
  .section--logo { top: 0; height: 490px; background: var(--stage-top); }
  .section--cards { top: 490px; height: 980px; background: var(--stage-cards); }
  .section--letter { top: 1470px; height: 810px; background: var(--stage-letter); }
  .section--envelopes { top: 2280px; height: 814px; background: var(--stage-env); }

  .paper { position: absolute; background: var(--paper); box-shadow: 0 2px 0 var(--edge), 0 12px 30px rgba(0,0,0,.08); }

  /* brand name block */
  .brand { display: flex; align-items: center; gap: .45em; font-weight: 700; color: var(--ink-dark); white-space: nowrap; letter-spacing: .02em; }
  .brand__square { width: .7em; height: .7em; background: var(--brand-blue); flex: none; }

  .section--logo .brand { position: absolute; top: 205px; left: 0; width: 1200px; justify-content: center; font-size: 58px; }

  /* business cards */
  .card { width: 560px; height: 320px; }
  .card--front { left: 90px; top: 120px; }
  .card--front .brand { position: absolute; inset: 0; justify-content: center; font-size: 30px; }
  .card--back { left: 550px; top: 520px; padding: 36px 40px; }
  .card--back .brand { position: absolute; top: 40px; right: 40px; font-size: 20px; }
  .card__rule { position: absolute; left: 40px; right: 40px; top: 110px; height: 1.5px; background: var(--brand-blue); }
  .card__person { position: absolute; left: 40px; top: 140px; }
  .card__name { font-weight: 600; font-size: 18px; letter-spacing: .03em; text-transform: uppercase; }
  .card__role { color: var(--brand-blue); font-size: 14px; }
  .contact { list-style: none; font-size: 13px; color: var(--ink-body); margin-top: 12px; }
  .contact li { display: flex; align-items: center; gap: 8px; line-height: 1.55; }
  .contact svg { width: 12px; height: 12px; flex: none; }
  .card__address { position: absolute; right: 40px; top: 140px; text-align: right; font-size: 13px; color: var(--ink-body); line-height: 1.5; }

  /* letterhead */
  .letter { left: 150px; top: 50px; width: 500px; height: 707px; padding: 60px 50px; font-size: 9px; color: var(--ink-body); line-height: 1.6; }
  .letter .brand { position: absolute; top: 52px; right: 50px; font-size: 15px; }
  .letter__salutation { margin-top: 80px; margin-bottom: 10px; }
  .letter p { margin-bottom: 10px; }
  .letter__signature { width: 70px; height: 30px; margin: 6px 0 24px; background: linear-gradient(90deg, #f3f3f3, #e6e6e6); }
  .letter .contact { position: absolute; left: 50px; bottom: 60px; font-size: 9px; }
  .letter .contact svg { width: 9px; height: 9px; }
  .letter__address { position: absolute; right: 50px; bottom: 40px; text-align: right; }
  .letter__address strong { color: var(--brand-blue); font-weight: 500; }

  /* envelopes */
  .envelope { width: 560px; height: 280px; }
  .envelope__flap { position: absolute; left: 0; right: 0; top: 0; height: 70px; border-bottom: 1px solid #eeeeee; }
  .envelope .brand { position: absolute; font-size: 15px; }
  .envelope--on-letter { left: 560px; top: 360px; }
  .envelope--on-letter .brand { top: 100px; left: 190px; }
  .envelope--back { left: 400px; top: 90px; }
  .envelope--back .brand { top: 110px; left: 190px; }
  .envelope--front { left: 130px; top: 420px; padding: 30px 34px; }
  .envelope--front .brand { top: 30px; left: 34px; }
  .envelope__sender { position: absolute; top: 62px; left: 34px; font-size: 10px; color: var(--ink-body); line-height: 1.5; }
  .envelope__pattern { position: absolute; right: 60px; bottom: 30px; width: 200px; height: 140px; background: linear-gradient(135deg, var(--faint-square), #f6f6f6); }
</style>
</head>
<body>

<section class="section section--logo">
  <div class="brand"><span class="brand__square"></span>BRISK TECHNOLOGY GMBH</div>
</section>

<section class="section section--cards">
  <div class="paper card card--front">
    <div class="brand"><span class="brand__square"></span>BRISK TECHNOLOGY GMBH</div>
  </div>

  <div class="paper card card--back">
    <div class="brand"><span class="brand__square"></span>BRISK TECHNOLOGY GMBH</div>
    <div class="card__rule"></div>
    <div class="card__person">
      <div class="card__name">Martin Keller</div>
      <div class="card__role">Geschäftsinhaber</div>
      <ul class="contact">
        <li><svg viewBox="0 0 12 12"><path fill="#2a93d5" d="M2.5 1l2 2.3-1 1.2a7 7 0 0 0 4 4l1.2-1 2.3 2-1.3 1.5C5.5 10.6 1.4 6.5 1 2.3z"/></svg>+41 79 555 12 34</li>
        <li><svg viewBox="0 0 12 12"><rect x="1" y="2.5" width="10" height="7" rx="1" fill="#2a93d5"/><path d="M1.5 3l4.5 3.5L10.5 3" stroke="#fff" fill="none"/></svg>martin.keller@brisk-technology.ch</li>
        <li><svg viewBox="0 0 12 12"><circle cx="6" cy="6" r="4.7" fill="none" stroke="#2a93d5" stroke-width="1.2"/><path d="M1.5 6h9M6 1.3c-2.5 3-2.5 6.4 0 9.4M6 1.3c2.5 3 2.5 6.4 0 9.4" stroke="#2a93d5" fill="none"/></svg>www.brisk-technology.ch</li>
      </ul>
    </div>
    <div class="card__address">Brisk Technology GmbH<br>Lindenweg 12<br>CH - 8000 Musterdorf</div>
  </div>
</section>

<section class="section section--letter">
  <div class="paper letter">
    <div class="brand"><span class="brand__square"></span>BRISK TECHNOLOGY GMBH</div>
    <div class="letter__salutation">Dear customer,</div>
    <p>We are pleased to confirm our meeting next week and look forward to discussing your energy and information technology plans in detail.</p>
    <p>Our team brings many years of experience in consulting and board mandates, and we will prepare a short summary of our proposed approach before the session.</p>
    <p>Please let us know if any further documents are required.</p>
    <div>Yours sincerely,</div>
    <div class="letter__signature" role="img" aria-label="Handwritten signature"></div>
    <ul class="contact">
      <li><svg viewBox="0 0 12 12"><path fill="#2a93d5" d="M2.5 1l2 2.3-1 1.2a7 7 0 0 0 4 4l1.2-1 2.3 2-1.3 1.5C5.5 10.6 1.4 6.5 1 2.3z"/></svg>+41 79 555 12 34</li>
      <li><svg viewBox="0 0 12 12"><rect x="1" y="2.5" width="10" height="7" rx="1" fill="#2a93d5"/></svg>martin.keller@brisk-technology.ch</li>
      <li><svg viewBox="0 0 12 12"><circle cx="6" cy="6" r="4.7" fill="none" stroke="#2a93d5" stroke-width="1.2"/></svg>www.brisk-technology.ch</li>
    </ul>
    <div class="letter__address"><strong>Brisk Technology GmbH</strong><br>Lindenweg 12<br>CH - 8000 Musterdorf</div>
  </div>

  <div class="paper envelope envelope--on-letter">
    <div class="envelope__flap"></div>
    <div class="brand"><span class="brand__square"></span>BRISK TECHNOLOGY</div>
  </div>
</section>

<section class="section section--envelopes">
  <div class="paper envelope envelope--back">
    <div class="envelope__flap"></div>
    <div class="brand"><span class="brand__square"></span>BRISK TECHNOLOGY</div>
  </div>

  <div class="paper envelope envelope--front">
    <div class="brand"><span class="brand__square"></span>BRISK TECHNOLOGY</div>
    <div class="envelope__sender">Lindenweg 12<br>CH - 8000 Musterdorf</div>
    <div class="envelope__pattern" role="img" aria-label="Faint decorative brand pattern"></div>
  </div>
</section>

</body>
</html>
```